Hvac and insulation company needs good looking business card design

We are hvac and insulation company and looking for a new business cards that look to today standards designs

Target Market(s)

homeowners

Industry/Entity Type

Hvac

Contact Information for Business Card

Name: Walter Brindley
Home comfort consultant
address: 4827 Moravia Ct #215 Oakland, CA 94602
office: 888-731-5096
cell: 510-842-3917
Lic.# 583164
Email: walter@corvane-hvac.example
Web: corvane-hvac.example

Requirements
Must have
• clean and sleek look
Nice to have
• simple with a clean look
Should not have
• to busy business card

```html
<!DOCTYPE html>
<html lang="en">
<head>
<meta charset="utf-8">
<title>Corvane Business Cards</title>
<link rel="stylesheet" href="https://fonts.googleapis.com/css2?family=Lato:wght@400;700&display=swap">
<style>
  :root {
    --brand-orange: #f58620;
    --card-white: #ffffff;
    --text-grey: #5a5a5a;
    --backdrop: #2d4a6a;
    --icon-grey: #6b6b6b;
  }
  * { box-sizing: border-box; margin: 0; padding: 0; }
  html, body { width: 1200px; height: 1000px; overflow: hidden; }
  body {
    background: var(--backdrop);
    font-family: "Lato", Arial, sans-serif;
    position: relative;
  }
  .card {
    position: absolute;
    width: 510px;
    height: 290px;
    overflow: hidden;
    box-shadow: 0 8px 18px rgba(0,0,0,0.35);
  }
  .card--rounded { border-radius: 34px; }
  .card--left { left: 62px; }
  .card--right { left: 624px; width: 512px; height: 292px; }
  .card--front { background: var(--brand-orange); }
  .card--back { background: var(--card-white); }
  .pos-top-left { top: 61px; }
  .pos-bottom-left { top: 428px; }
  .pos-top-right { top: 282px; }
  .pos-bottom-right { top: 638px; }

  .wordmark {
    display: flex;
    align-items: center;
    gap: 12px;
    font-weight: 700;
    line-height: 1;
  }
  .wordmark__dot { border-radius: 50%; flex: none; }
  .card--front .wordmark {
    position: absolute;
    left: 0; right: 0; top: 110px;
    justify-content: center;
    color: var(--card-white);
    font-size: 52px;
  }
  .card--front .wordmark__dot { width: 44px; height: 44px; background: var(--card-white); }
  .front-web {
    position: absolute;
    left: 0; right: 0; bottom: 16px;
    text-align: center;
    color: var(--card-white);
    font-size: 15px;
  }

  .card--back .wordmark {
    position: absolute;
    right: 22px; top: 34px;
    color: var(--brand-orange);
    font-size: 36px;
  }
  .card--back .wordmark__dot { width: 32px; height: 32px; background: var(--brand-orange); }
  .holder-name {
    position: absolute;
    left: 26px; top: 82px;
    font-size: 27px;
    color: var(--text-grey);
  }
  .holder-title {
    position: absolute;
    left: 26px; top: 114px;
    font-size: 16px;
    color: var(--text-grey);
  }
  .rule {
    position: absolute;
    left: 24px; right: 0; top: 141px;
    height: 2px;
    background: var(--brand-orange);
  }
  .address-band {
    position: absolute;
    left: 154px; right: 0; top: 141px;
    height: 26px;
    background: var(--brand-orange);
    clip-path: polygon(0 0, 100% 0, 100% 100%, 16px 100%);
    color: var(--card-white);
    font-size: 14px;
    text-align: right;
    padding: 4px 22px 0 0;
  }
  .contact-list {
    position: absolute;
    left: 26px; top: 182px;
    list-style: none;
    color: var(--text-grey);
    font-size: 18px;
  }
  .contact-list li { display: flex; align-items: center; gap: 12px; height: 27px; }
  .contact-list li:last-child { height: 22px; font-size: 17.5px; }
  .contact-list svg { width: 15px; height: 15px; fill: var(--icon-grey); flex: none; }
  .licence {
    position: absolute;
    right: 22px; bottom: 24px;
    font-size: 13px;
    color: var(--text-grey);
  }
</style>
</head>
<body>

<section class="card card--front card--rounded card--left pos-top-left">
  <div class="wordmark"><span class="wordmark__dot"></span>corvane</div>
  <p class="front-web">www.corvane-hvac.example</p>
</section>

<section class="card card--back card--rounded card--left pos-bottom-left">
  <div class="wordmark"><span class="wordmark__dot"></span>corvane</div>
  <h1 class="holder-name">Walter Brindley</h1>
  <p class="holder-title">Home comfort consultant</p>
  <div class="rule"></div>
  <div class="address-band">4827 Moravia Ct #215 Oakland, CA 94602</div>
  <ul class="contact-list">
    <li><svg viewBox="0 0 16 16"><path d="M1 5c0-2 3-3 7-3s7 1 7 3v1h-3V5H4v1H1zM3 7h10l1 7H2zm5 2a2 2 0 1 0 0 4 2 2 0 0 0 0-4z"/></svg>888-731-5096</li>
    <li><svg viewBox="0 0 16 16"><path d="M3 1l3 3-2 2c1 2 4 5 6 6l2-2 3 3-2 2C7 15 1 9 1 3z"/></svg>510-842-3917</li>
    <li><svg viewBox="0 0 16 16"><path d="M1 4h14v9H1zm1 1l6 4 6-4"/></svg>walter@corvane-hvac.example</li>
  </ul>
  <p class="licence">Lic.# 583164</p>
</section>

<section class="card card--front card--right pos-top-right">
  <div class="wordmark"><span class="wordmark__dot"></span>corvane</div>
  <p class="front-web">www.corvane-hvac.example</p>
</section>

<section class="card card--back card--right pos-bottom-right">
  <div class="wordmark"><span class="wordmark__dot"></span>corvane</div>
  <h1 class="holder-name">Walter Brindley</h1>
  <p class="holder-title">Home comfort consultant</p>
  <div class="rule"></div>
  <div class="address-band">4827 Moravia Ct #215 Oakland, CA 94602</div>
  <ul class="contact-list">
    <li><svg viewBox="0 0 16 16"><path d="M1 5c0-2 3-3 7-3s7 1 7 3v1h-3V5H4v1H1zM3 7h10l1 7H2zm5 2a2 2 0 1 0 0 4 2 2 0 0 0 0-4z"/></svg>888-731-5096</li>
    <li><svg viewBox="0 0 16 16"><path d="M3 1l3 3-2 2c1 2 4 5 6 6l2-2 3 3-2 2C7 15 1 9 1 3z"/></svg>510-842-3917</li>
    <li><svg viewBox="0 0 16 16"><path d="M1 4h14v9H1zm1 1l6 4 6-4"/></svg>walter@corvane-hvac.example</li>
  </ul>
  <p class="licence">Lic.# 583164</p>
</section>

</body>
</html>
```